Professional University Report Template

I have the need for a professionally-designed, multi-page report template, consisting of 8.5 x 11 inch pages - like a book, but not facing page design. An InDesign template would be best for my purposes.

This is a professional document in which I will need a main column for text, and a side column (around 1/3 of the width) to include photos, graphics, quotes, and lists. No background colors should be used, but perhaps some shading would be fine. This will be distributed as a PDF and will be printed by many in greyscale - so it should look great, and be easy to view without color.

As it is for a university publication, it must be overall professional and a bit subdued. The design should not overshadow the content, but enhance the overall experience. Most of all, I am aiming for something that is original and interesting.

Target Market(s)

University professors

Industry/Entity Type

University

Requirements
Must have
• Title page

Then a 3-page example document (use the text from sample indicator doc file):
Header 1 text
Header 2 text
body text
bulleted list
footer text noting the chapter title and page number

In the side columns of example pages (use the image files):
Photos
graphs
quoted text
bulleted list
Should not have
• No need for table of contents page, logo placement, or headers

```html
<!DOCTYPE html>
<html lang="en">
<head>
<meta charset="utf-8">
<title>Department activity</title>
<link href="https://fonts.googleapis.com/css2?family=Crimson+Text:ital,wght@0,400;0,600;0,700;1,400;1,600&display=swap" rel="stylesheet">
<style>
  :root {
    --ink: #1a1a1a;
    --rule: #000000;
    --rule-thin: #555555;
    --mark: #d9d9d9;
    --caption-bg: #0d0d0d;
    --caption-ink: #ffffff;
    --muted: #8a8a8a;
    --paper: #ffffff;
  }
  * { margin: 0; padding: 0; box-sizing: border-box; }
  html, body { width: 927px; height: 1200px; overflow: hidden; background: var(--paper); }
  body { font-family: "Crimson Text", Georgia, serif; color: var(--ink); }
  .page { position: relative; width: 927px; height: 1200px; }

  .page-header { position: absolute; left: 84px; top: 70px; width: 762px; }
  .quote-mark { position: absolute; font-size: 100px; line-height: 1; color: var(--mark); font-weight: 700; }
  .quote-mark.open { left: -6px; top: 24px; }
  .quote-mark.close { right: -4px; top: 20px; }
  .section-title { position: relative; font-size: 35px; font-weight: 700; line-height: 1.1; white-space: nowrap; }
  .section-subtitle { position: relative; font-size: 24.5px; font-weight: 700; line-height: 1.2; margin-top: 4px; white-space: nowrap; letter-spacing: -0.1px; }

  .header-rule { position: absolute; left: 84px; top: 172px; width: 762px; height: 5px; }
  .header-rule .thick { position: absolute; left: 0; top: 0; width: 502px; height: 4px; background: var(--rule); border-radius: 0 2px 2px 0; }
  .header-rule .thin { position: absolute; left: 502px; top: 2px; right: 0; height: 1px; background: var(--rule-thin); }

  .main-column { position: absolute; left: 85px; top: 210px; width: 500px; font-size: 13.6px; line-height: 19.7px; text-align: justify; }
  .main-column p { margin-bottom: 19.7px; }
  .lead { font-weight: 700; }
  .drop-cap { float: left; font-size: 62px; line-height: 50px; font-weight: 600; margin: 2px 5px 0 0; }

  .pull-quotes { position: relative; padding-left: 33px; margin: 0 0 19px; font-style: italic; }
  .pull-quotes .brace { position: absolute; left: -6px; top: -12px; font-size: 106px; line-height: 1; color: var(--mark); font-style: normal; font-weight: 400; }
  .pull-quotes p { margin-bottom: 16px; text-indent: -6px; padding-left: 6px; }
  .pull-quotes p:last-child { margin-bottom: 0; }

  .side-photo { position: absolute; left: 601px; width: 244px; }
  .side-photo .photo { width: 100%; display: block; }
  .side-photo .caption { background: var(--caption-bg); color: var(--caption-ink); font-style: italic; font-weight: 600; font-size: 12px; padding: 2px 6px 3px; }
  .photo-classroom { top: 373px; }
  .photo-classroom .photo { height: 161px; background: linear-gradient(160deg, #8d8a80 0%, #6f6a5f 45%, #b7b6b9 100%); }
  .photo-visit { top: 936px; }
  .photo-visit .photo { height: 160px; background: linear-gradient(150deg, #6e5d46 0%, #4a3f33 50%, #9a9aa0 100%); }

  .page-footer { position: absolute; left: 0; width: 927px; top: 1128px; text-align: center; font-size: 12px; }
  .page-footer .number { color: var(--ink); padding-right: 6px; border-right: 1px solid var(--ink); }
  .page-footer .chapter { color: var(--muted); padding-left: 6px; }
</style>
</head>
<body>
<div class="page">
  <header class="page-header">
    <span class="quote-mark open">&ldquo;</span>
    <span class="quote-mark close">&rdquo;</span>
    <h1 class="section-title">Department activity:</h1>
    <h2 class="section-subtitle">Evidence of revision of existing courses that significantly improve them</h2>
  </header>
  <div class="header-rule"><span class="thick"></span><span class="thin"></span></div>

  <main class="main-column">
    <p class="lead"><span class="drop-cap">S</span>ervice learning is the most important pedagogical concept that I have embraced since starting at Ridgeview State University. I was introduced to service learning through the Campus and Community Together (CCT) office here on campus, and was selected as a cct faculty fellow for the 2009-2010 academic year. Faculty fellows in service learning attend a series of workshops on aspects of this pedagogical model, and develop syllabi, or enhancing existing syllabus, to integrate service learning activities into a course.</p>

    <p>In preparation of the international service learning project, I wrote a grant proposal for the successful applications of learning technologies (salt) grant offered by the Harlow College of education for the academic year 2010 2011. The application I spent on the idea of internationalizing the web design course through an international service learning project with partner organizations in the southern state of Tamil Nadu, Indian. The International Office here Ridgeview State connected me with community partners in the cities of Chennai and monitor I, whom I contacted about the project ideas. Grant was successfully funded, allowing me to travel to Chennai and Madurai to meet with the partners and to expand on the project ideas that students will be engaged in for the spring semester 2011.</p>

    <p>Student groups were challenged with developing projects to assist the community organizations with their web development needs. I go was pursuing factors technology mentors for the groups and southern India, to medicating with them via e-mail and posting website designs and ideas through online services such as voice to solicit comments and reactions to the web design. Student feedback for the 1st implementation of this in the course was primarily positive. The following quotes were taken from the end of the semester course evaluations:</p>

    <blockquote class="pull-quotes">
      <span class="brace">{</span>
      <p>&ldquo;This was a great project, it helped me understand much more about technology and communicating with others&rdquo;</p>
      <p>&ldquo;My partner in India and I have become great friends, thanks for letting us have this opportunity to connect with others on the other side of the world&rdquo;</p>
    </blockquote>

    <p>This project serves as a model for service learning program international service learning projects. I presented a poster session at the 2010 society for learning technology in education (slte) international conference in Charleston, South Carolina. In addition, the course ideas were featured on the Ridgeview State home page in an article related to international service learning projects at the University.</p>

    <p>I have continued to collaborate with partner organizations in Chennai, inviting them to work with students in my courses in the past few years. One recent example is Meera from the Chennai community, who was a guest car ITC 5620 course in the spring 2012 semester. I&rsquo;ve also introduced service learning into other courses, for instance a community based project in our introductory eye to see 50 to 20 course, where students create mobile learning activities for the public available at the Millbrook Greenway, a popular recreation area in town.</p>
  </main>

  <figure class="side-photo photo-classroom">
    <div class="photo" role="img" aria-label="Photo of schoolchildren in uniforms seated on the floor of a classroom"></div>
    <figcaption class="caption">Lorem Ipsum</figcaption>
  </figure>

  <figure class="side-photo photo-visit">
    <div class="photo" role="img" aria-label="Photo of a teacher and a visiting faculty member standing with students in a classroom"></div>
    <figcaption class="caption">Lorem Ipsum</figcaption>
  </figure>

  <footer class="page-footer"><span class="number">2</span><span class="chapter">Department activity</span></footer>
</div>
</body>
</html>
```